Analytics software company needs a business card design

We need a business card design for a global analytics software provider called 'Varnel Software'. Our main focus is developing real estate analysis software. We are open to any color scheme. The final design should be simple, modern, and precise.
Updates

There is one day left in our project and we are still looking forward to receiving additional submissions. We look forward to selecting one of your designs. Thanks.

Industry/Entity Type

Real Estate

```html
<!DOCTYPE html>
<html lang="en">
<head>
<meta charset="utf-8">
<title>Varnel Software – Business Card</title>
<link rel="stylesheet" href="https://fonts.googleapis.com/css2?family=Roboto:wght@400;500&display=swap">
<style>
  :root {
    --stage: #1b1b1d;
    --card: #333436;
    --rule: #8a8b8d;
    --ink: #ffffff;
    --blue: #1e9ad6;
    --green: #7cbb42;
    --orange: #f39a1e;
  }
  * { margin: 0; padding: 0; box-sizing: border-box; }
  html, body { width: 1200px; height: 900px; overflow: hidden; }
  body {
    background: var(--stage);
    font-family: "Roboto", Arial, sans-serif;
    position: relative;
  }
  .card {
    position: absolute;
    left: 280px;
    width: 640px;
    height: 366px;
    background: var(--card);
    border-radius: 3px;
    overflow: hidden;
  }
  .card--front { top: 59px; }
  .card--back { top: 475px; }
  .card svg { position: absolute; inset: 0; }

  .legend {
    position: absolute; left: 60px; top: 180px;
    list-style: none;
  }
  .legend li {
    display: flex; align-items: center;
    gap: 8px; color: var(--ink); font-size: 11px; line-height: 20px; letter-spacing: 0.4px;
  }
  .legend i { display: block; width: 10px; height: 10px; border-radius: 50%; }
  .brand-title {
    position: absolute; left: 60px; top: 58px;
    color: var(--blue); font-size: 31px; font-weight: 500; letter-spacing: 0.5px;
  }
  .brand-tagline {
    position: absolute; left: 60px; top: 100px;
    color: var(--ink); font-size: 12px; letter-spacing: 1.2px;
  }

  .person { position: absolute; left: 50px; top: 150px; }
  .person-name { color: var(--blue); font-size: 26px; font-weight: 400; letter-spacing: 0.5px; }
  .person-title { color: var(--ink); font-size: 12px; margin-top: 4px; letter-spacing: 0.3px; }

  .contact { position: absolute; left: 50px; top: 244px; list-style: none; }
  .contact li { color: var(--ink); font-size: 13px; line-height: 19px; }
  .contact b { color: var(--blue); font-weight: 400; display: inline-block; width: 14px; }
  .social { position: absolute; left: 50px; top: 312px; color: var(--blue); font-size: 13px; }

  .company { position: absolute; left: 360px; top: 150px; font-size: 12px; line-height: 17px; color: var(--ink); }
  .company-name { color: var(--blue); font-size: 13px; }
  .company-web { color: var(--orange); margin-top: 18px; font-size: 13px; }
</style>
</head>
<body>

<section class="card card--front">
  <svg viewBox="0 0 640 366" aria-hidden="true">
    <g stroke="var(--rule)" stroke-width="1">
      <line x1="300" y1="130" x2="610" y2="130"/>
      <line x1="300" y1="170" x2="610" y2="170"/>
      <line x1="300" y1="210" x2="610" y2="210"/>
      <line x1="300" y1="250" x2="610" y2="250"/>
      <line x1="300" y1="290" x2="610" y2="290"/>
      <line x1="300" y1="330" x2="610" y2="330"/>
    </g>
    <g class="bars">
      <rect x="318" y="270" width="14" height="60" fill="var(--blue)"/>
      <rect x="334" y="240" width="14" height="90" fill="var(--green)"/>
      <rect x="378" y="225" width="14" height="105" fill="var(--blue)"/>
      <rect x="394" y="255" width="14" height="75" fill="var(--green)"/>
      <rect x="438" y="195" width="14" height="135" fill="var(--blue)"/>
      <rect x="454" y="215" width="14" height="115" fill="var(--green)"/>
      <rect x="498" y="180" width="14" height="150" fill="var(--blue)"/>
      <rect x="514" y="160" width="14" height="170" fill="var(--green)"/>
      <rect x="558" y="145" width="14" height="185" fill="var(--blue)"/>
      <rect x="574" y="150" width="14" height="180" fill="var(--green)"/>
    </g>
    <polyline points="325,300 385,285 445,240 505,225 565,190" fill="none" stroke="var(--orange)" stroke-width="2.5"/>
  </svg>
  <h1 class="brand-title">VARNEL SOFTWARE</h1>
  <p class="brand-tagline">REAL ESTATE ANALYTICS</p>
  <ul class="legend">
    <li><i style="background:var(--blue)"></i>SALES</li>
    <li><i style="background:var(--green)"></i>RENTALS</li>
    <li><i style="background:var(--orange)"></i>TREND</li>
  </ul>
</section>

<section class="card card--back">
  <svg viewBox="0 0 640 366" aria-hidden="true">
    <line x1="50" y1="60" x2="610" y2="60" stroke="var(--rule)" stroke-width="1"/>
    <line x1="50" y1="228" x2="300" y2="228" stroke="var(--rule)" stroke-width="1"/>
    <rect x="0" y="358" width="214" height="8" fill="var(--blue)"/>
    <rect x="214" y="358" width="213" height="8" fill="var(--green)"/>
    <rect x="427" y="358" width="213" height="8" fill="var(--orange)"/>
  </svg>
  <div class="person">
    <h2 class="person-name">DANA WHITFORD</h2>
    <p class="person-title">YOUR TITLE HERE</p>
  </div>
  <ul class="contact">
    <li><b>P</b>123.465.7895</li>
    <li><b>F</b>123.456.7890</li>
    <li><b>E</b>DANA@VARNELSOFTWARE.COM</li>
  </ul>
  <p class="social">SOCIAL.VARNELSOFTWARE.COM</p>
  <div class="company">
    <p class="company-name">VARNEL SOFTWARE LLC</p>
    <p>4200 HARLOW CREST RD</p>
    <p>LINDEN PARK, MD 20910, USA</p>
    <p class="company-web">WWW.VARNELSOFTWARE.COM</p>
  </div>
</section>

</body>
</html>
```